Business Card Design Project

We need a business card design for a new boutique consulting company, LumaConsulting. Our new logo has just been designed and we are looking for simple, clean looking business cards. Logo attached

Industry/Entity Type

Boutique

Requirements
Must have
• There must be room for each card to have the following details:
Name
Title
Address - 2 lines
Phone number
Email address
Website address

Nice to have
• May have something on the back of the buisness card - emphasing the word "Luma".

```html
<!DOCTYPE html>
<html lang="en">
<head>
<meta charset="utf-8">
<title>LumaConsulting – Business Cards</title>
<link rel="stylesheet" href="https://fonts.googleapis.com/css2?family=Questrial&display=swap">
<style>
  :root {
    --page-bg: #e6e6e6;
    --lime: #c4f25a;
    --green: #8cc43f;
    --green-deep: #7ab334;
    --card-white: #ffffff;
    --ink-grey: #8a8a8a;
    --ink-soft: #9a9a9a;
    --shadow: rgba(0, 0, 0, 0.18);
  }
  * { box-sizing: border-box; margin: 0; padding: 0; }
  html, body {
    width: 1200px;
    height: 800px;
    overflow: hidden;
  }
  body {
    background: var(--page-bg);
    font-family: "Questrial", "Century Gothic", sans-serif;
    position: relative;
  }
  .card {
    position: absolute;
    top: 250px;
    width: 500px;
    height: 300px;
    border-radius: 16px;
    overflow: hidden;
    box-shadow: 0 6px 18px var(--shadow);
  }

  /* Back of card */
  .card--back {
    left: 70px;
    background: linear-gradient(135deg, var(--lime) 0%, var(--green) 70%, var(--green-deep) 100%);
  }
  .card--back .brand-name {
    position: absolute;
    left: 52px;
    bottom: 62px;
    font-size: 50px;
    letter-spacing: -0.5px;
    color: var(--ink-grey);
  }

  /* Front of card */
  .card--front {
    left: 630px;
    background: var(--card-white);
  }
  .card--front .brand-name {
    position: absolute;
    left: 38px;
    top: 26px;
    font-size: 42px;
    letter-spacing: -0.5px;
    color: var(--green);
  }
  .brand-mark {
    display: inline-block;
    width: 12px;
    height: 12px;
    margin-right: 10px;
    vertical-align: middle;
    background: var(--green);
  }
  .card--back .brand-mark { background: var(--ink-grey); }

  .person {
    position: absolute;
    left: 40px;
    top: 92px;
    color: var(--ink-grey);
    font-size: 24px;
    line-height: 1.15;
    letter-spacing: 0.5px;
  }
  .contact {
    position: absolute;
    right: 32px;
    bottom: 22px;
    text-align: right;
    font-style: normal;
    color: var(--ink-soft);
    font-size: 19px;
    line-height: 1.3;
    letter-spacing: 0.5px;
  }
  .contact span { display: block; }
</style>
</head>
<body>
  <section class="card card--back" aria-label="Card back">
    <p class="brand-name"><span class="brand-mark"></span>LumaConsulting</p>
  </section>

  <section class="card card--front" aria-label="Card front">
    <p class="brand-name"><span class="brand-mark"></span>LumaConsulting</p>
    <p class="person">
      <span class="person-name">Mara Holt</span><br>
      <span class="person-title">Director</span>
    </p>
    <address class="contact">
      <span>Elm Row 27</span>
      <span>Brookvale, 40218</span>
      <span>+00 245 671 908</span>
      <span>mholt@lumaconsulting.com</span>
      <span>www.lumaconsulting.com</span>
    </address>
  </section>
</body>
</html>
```